Business Card for Wellness Clinic

We need a business card for our new logo. I want it to match the feel of the logo

Target Market(s)

Young professional families looking for holistic health care

Industry/Entity Type

Health And Wellness

Contact Information for Business Card

Our business Name: Brackenfield Health & wellness Centre, our phone #, email address...see attached old business card

Font styles to use
Sans Serif

Colors
33b8a4
cee9f5

Requirements
Must have
• my logo and business name
• Font is "Helvetica Neue LT Std 45 Light" and
• Only for "&" using font "Trajan pro bold"
• Use colors in the logo

```html
<!DOCTYPE html>
<html lang="en">
<head>
<meta charset="utf-8">
<title>Brackenfield Health &amp; wellness Centre – Business Card</title>
<link rel="stylesheet" href="https://fonts.googleapis.com/css2?family=Arimo:wght@400;700&family=Tinos:wght@400;700&display=swap">
<style>
  :root {
    --teal: #33b8a4;
    --teal-deep: #2aa591;
    --sky: #cee9f5;
    --grey: #a9acae;
    --grey-text: #9a9c9e;
    --ink: #1b1b1b;
    --paper: #ffffff;
    --backdrop: #ebe8e3;
  }
  * { box-sizing: border-box; margin: 0; padding: 0; }
  html, body { width: 1200px; height: 864px; overflow: hidden; }
  body {
    background: var(--backdrop);
    font-family: "Arimo", "Helvetica Neue", Arial, sans-serif;
    color: var(--ink);
    position: relative;
  }
  .card {
    position: absolute;
    width: 540px;
    height: 308px;
    background: var(--paper);
    box-shadow: 0 6px 18px rgba(0,0,0,.14);
    overflow: hidden;
  }
  .card--front { left: 40px; top: 278px; }
  .card--back  { left: 620px; top: 278px; }

  .card__shapes { position: absolute; inset: 0; }

  .brand-mark {
    position: absolute;
    left: 52px; top: 92px;
    display: flex; align-items: center; gap: 10px;
    font-family: "Tinos", "Times New Roman", serif;
    font-weight: 700;
    font-size: 26px;
    color: var(--teal);
  }
  .brand-mark__dot {
    width: 16px; height: 16px; border-radius: 50%;
    background: var(--teal);
  }

  .business-name {
    position: absolute;
    right: 24px; top: 58px;
    width: 250px;
    text-align: right;
  }
  .business-name__main {
    font-size: 16px;
    letter-spacing: 5px;
    color: var(--grey-text);
    font-weight: 400;
    border-bottom: 1px solid #c9cbcc;
    padding-bottom: 3px;
  }
  .business-name__amp {
    font-family: "Tinos", serif;
    font-weight: 700;
    font-size: 9px;
    color: var(--grey-text);
    text-align: center;
    margin: 1px 0 -2px;
  }
  .business-name__sub {
    font-size: 9px;
    letter-spacing: 7px;
    color: var(--teal);
  }

  .contact {
    position: absolute;
    right: 26px; top: 166px;
    text-align: right;
  }
  .contact__name {
    font-family: "Tinos", serif;
    font-weight: 700;
    font-size: 21px;
    color: var(--ink);
  }
  .contact__title {
    font-family: "Tinos", serif;
    font-size: 14px;
    margin-bottom: 10px;
  }
  .contact__line {
    font-size: 12px;
    line-height: 17px;
    display: flex; justify-content: flex-end; align-items: center; gap: 6px;
  }
  .contact__icon {
    width: 11px; height: 11px; background: var(--ink);
    display: inline-block; flex: none;
  }

  .appointment__title {
    position: absolute;
    left: 0; right: 0; top: 34px;
    padding-left: 190px;
    font-family: "Tinos", serif;
    font-size: 30px;
    color: var(--teal);
  }
  .appointment__field {
    position: absolute;
    font-family: "Arimo", sans-serif;
    font-weight: 700;
    font-size: 13px;
    display: flex; align-items: flex-end;
  }
  .appointment__rule {
    flex: 1;
    border-bottom: 1.5px dotted var(--ink);
    margin-left: 3px;
    height: 11px;
  }
  .field-date { left: 30px; right: 30px; top: 82px; }
  .field-for  { left: 30px; width: 250px; top: 104px; }
  .field-time { left: 286px; right: 30px; top: 104px; }
  .appointment__days {
    position: absolute;
    left: 30px; right: 24px; top: 138px;
    display: flex; justify-content: space-between;
    font-size: 13px;
  }
  .appointment__day { display: flex; align-items: center; gap: 3px; }
  .appointment__box {
    width: 12px; height: 12px; border: 1.2px solid var(--ink);
  }
  .appointment__line {
    position: absolute; left: 30px; right: 30px;
    border-bottom: 1.5px dotted var(--ink);
  }
  .line-one { top: 180px; }
  .line-two { top: 208px; }
  .watermark-name {
    position: absolute;
    right: 28px; top: 226px;
    font-family: "Tinos", serif;
    font-weight: 700;
    font-size: 40px;
    color: var(--teal);
    opacity: .2;
  }
</style>
</head>
<body>

  <section class="card card--front" aria-label="Business card front">
    <svg class="card__shapes" width="540" height="308" viewBox="0 0 540 308" aria-hidden="true">
      <polygon points="292,148 540,148 540,308 60,308" fill="var(--teal)"/>
      <polyline points="252,0 290,142 46,308" fill="none" stroke="var(--grey)" stroke-width="7"/>
      <line x1="262" y1="0" x2="298" y2="138" stroke="var(--teal)" stroke-width="3"/>
    </svg>

    <div class="brand-mark">
      <span class="brand-mark__dot"></span>
      <span>Brackenfield</span>
    </div>

    <div class="business-name">
      <div class="business-name__main">BRACKENFIELD HEALTH</div>
      <div class="business-name__amp">&amp;</div>
      <div class="business-name__sub">WELLNESS CENTRE</div>
    </div>

    <div class="contact">
      <div class="contact__name">Dr. Helena Marsh, N.D</div>
      <div class="contact__title">Naturopathic Doctor</div>
      <div class="contact__line">613-555-0142 <span class="contact__icon"></span></div>
      <div class="contact__line">www.marshnaturopathic.ca <span class="contact__icon"></span></div>
      <div class="contact__line">hmarsh@marshnaturopathic.ca <span class="contact__icon"></span></div>
      <div class="contact__line">48 linden ave.w, Suite 210 Ottawa, ON K2P 3R7 <span class="contact__icon"></span></div>
    </div>
  </section>

  <section class="card card--back" aria-label="Appointment card back">
    <div class="watermark-name">Brackenfield</div>
    <h1 class="appointment__title">Appointment</h1>
    <div class="appointment__field field-date">Date:<span class="appointment__rule"></span></div>
    <div class="appointment__field field-for">For:<span class="appointment__rule"></span></div>
    <div class="appointment__field field-time">Time:<span class="appointment__rule"></span></div>
    <div class="appointment__days">
      <span class="appointment__day"><span class="appointment__box"></span>MON.</span>
      <span class="appointment__day"><span class="appointment__box"></span>TUE.</span>
      <span class="appointment__day"><span class="appointment__box"></span>WED.</span>
      <span class="appointment__day"><span class="appointment__box"></span>THUR.</span>
      <span class="appointment__day"><span class="appointment__box"></span>FRI.</span>
      <span class="appointment__day"><span class="appointment__box"></span>SAT.</span>
    </div>
    <div class="appointment__line line-one"></div>
    <div class="appointment__line line-two"></div>
  </section>

</body>
</html>
```